Bluestone Advisory & Mgmt - Professional Business Cards

Hi!

I am a Real Estate Developer and Construction Consultant.

I have a lot of inspiration from previous designs and would be open to using the attached Designs as a starting point. I would like to see these styles incorporated into your designs.

I really need professional business card to go with it that includes my important info.

Look forward to seeing your designs!.

Target Market(s)

My Target market are building owners, lawyers, consultants.

Industry/Entity Type

Real Estate Development

Contact Information for Business Card

My Name: Daniel Korvash
My Title: Principle
Company Name: Bluestone Advisory & Mgmt, LLC
Address: 348 West 41st Street, 7th FL New York, NY 10036
Mobile: 917.608.3719
Website: bam-hqx.com

Font styles to use
Serif
Sans Serif

Colors

Designer to choose colors to be used in the design.

Requirements
Must have
• Must incorporate the logo attached or have new that looks similar.
• Must use professional font that will be seen and judged by wealthy land owners and developers.
• Must incorporate some of the color green.
Should not have
• Photo's or pictures of people or buildings of any kind.

```html
<!DOCTYPE html>
<html lang="en">
<head>
<meta charset="utf-8">
<title>Bluestone Advisory &amp; Mgmt – Business Cards</title>
<link rel="stylesheet" href="https://fonts.googleapis.com/css2?family=Montserrat:wght@400;500;600;700&display=swap">
<style>
  :root {
    --bg-top: #3a3a3a;
    --bg-bottom: #141414;
    --card: #1f1f1f;
    --card-light: #2b2b2b;
    --green: #4cb87a;
    --white: #ffffff;
    --muted: #e6e6e6;
  }
  * { box-sizing: border-box; margin: 0; padding: 0; }
  html, body { width: 1200px; height: 900px; overflow: hidden; }
  body {
    background: radial-gradient(ellipse at 55% 30%, var(--bg-top), var(--bg-bottom) 75%);
    font-family: "Montserrat", sans-serif;
    position: relative;
  }
  .card {
    position: absolute;
    left: 250px;
    width: 700px;
    height: 400px;
    background: linear-gradient(135deg, var(--card) 0%, var(--card-light) 70%, var(--card) 100%);
    box-shadow: 0 18px 40px rgba(0,0,0,.55);
    overflow: hidden;
  }
  .card::after {
    content: "";
    position: absolute;
    left: 0; right: 0; bottom: 0;
    height: 8px;
    background: var(--green);
  }
  .card--front { top: 40px; }
  .card--back { top: 470px; }

  .brand-name {
    color: var(--green);
    font-weight: 600;
    line-height: 1.05;
    letter-spacing: .5px;
  }
  .card--front .brand-name {
    position: absolute;
    left: 0; right: 0; top: 150px;
    text-align: center;
    font-size: 44px;
  }
  .card--front .brand-mark {
    display: inline-block;
    width: 26px; height: 26px;
    background: var(--green);
    margin-right: 16px;
    vertical-align: 2px;
  }

  .card--back .brand-name {
    position: absolute;
    left: 44px; top: 130px;
    width: 300px;
    font-size: 40px;
  }
  .divider {
    position: absolute;
    left: 370px; top: 80px;
    width: 2px; height: 230px;
    background: var(--green);
  }
  .contact {
    position: absolute;
    left: 400px; top: 90px;
    color: var(--muted);
    font-size: 16px;
    line-height: 1.45;
  }
  .contact__name {
    color: var(--green);
    font-weight: 600;
    font-size: 25px;
    letter-spacing: 1.5px;
    text-transform: uppercase;
  }
  .contact__title { font-size: 17px; margin-bottom: 16px; }
  .contact__address { margin-bottom: 12px; }
  .contact__row { display: flex; align-items: center; gap: 10px; }
  .contact__row svg { width: 13px; height: 13px; flex: none; }
</style>
</head>
<body>
  <section class="card card--front">
    <div class="brand-name"><span class="brand-mark"></span>Bluestone<br>Advisory &amp; Mgmt</div>
  </section>

  <section class="card card--back">
    <div class="brand-name">Bluestone Advisory &amp; Mgmt</div>
    <div class="divider"></div>
    <div class="contact">
      <div class="contact__name">Daniel Korvash</div>
      <div class="contact__title">Principle</div>
      <div class="contact__address">348 West 41st Street,<br>7th FL New York, NY 10036</div>
      <div class="contact__row">
        <svg viewBox="0 0 16 16" aria-hidden="true"><path d="M4 1l3 3-2 2c1 2 3 4 5 5l2-2 3 3-2 2C7 14 2 9 2 3z" fill="var(--green)"/></svg>
        <span>917.608.3719</span>
      </div>
      <div class="contact__row">
        <svg viewBox="0 0 16 16" aria-hidden="true"><rect x="1" y="3" width="14" height="10" fill="none" stroke="var(--green)" stroke-width="1.5"/><path d="M1 3l7 6 7-6" fill="none" stroke="var(--green)" stroke-width="1.5"/></svg>
        <span>info@bam-hqx.com</span>
      </div>
      <div class="contact__row">
        <svg viewBox="0 0 16 16" aria-hidden="true"><circle cx="8" cy="8" r="6.5" fill="none" stroke="var(--green)" stroke-width="1.4"/><ellipse cx="8" cy="8" rx="3" ry="6.5" fill="none" stroke="var(--green)" stroke-width="1.2"/><path d="M1.5 8h13" stroke="var(--green)" stroke-width="1.2"/></svg>
        <span>www.bam-hqx.com</span>
      </div>
    </div>
  </section>
</body>
</html>
```